New Labels for VANTO Sports Drinks

Sports drink company looking for new fresh look with commercial appeal beverage labels. You can use the current label as a guide but adjust where you see fit. Would like to standout from other sports drink on store shelves. VANTO Sports Drinks is a fusion of real brewed tea and all natural electrolytes. Our tea features a bold, full-bodied flavor profile, combined with all natural electrolytes, giving you one of the very first tea based sports drinks.

Target Market(s)

16-40

Colors

Designer to choose colors to be used in the design.

Requirements
Must have
• Name
• flavor
• description
• nutritional info
• all Info on back of labels
Nice to have
• sports image
• fruit flavor
• white background
• Real tea and natural electrolytes
Should not have
• n/a

```html
<!DOCTYPE html>
<html lang="en">
<head>
<meta charset="utf-8">
<title>VANTO Sports Tea – Pineapple Label</title>
<link href="https://fonts.googleapis.com/css2?family=Anton&family=Montserrat:wght@700&family=Roboto+Condensed:wght@400;700&display=swap" rel="stylesheet">
<style>
  :root {
    --backdrop: #ffffff;
    --label-yellow: #f9dc72;
    --label-green: #14cc14;
    --band-green: #12c812;
    --ink: #111111;
    --outline-green: #2f7d1a;
    --volume-ink: #1b2a1b;
    --white: #ffffff;
    --cyclist-tone-a: #2a8a25;
    --cyclist-tone-b: #58b548;
    --runner-tone-a: #c2ad82;
    --runner-tone-b: #8a7758;
  }
  * { margin: 0; padding: 0; box-sizing: border-box; }
  html, body {
    width: 918px;
    height: 1200px;
    overflow: hidden;
    background: var(--backdrop);
  }
  .canvas {
    position: relative;
    width: 918px;
    height: 1200px;
  }
  .label {
    position: absolute;
    left: 129px;
    top: 32px;
    width: 660px;
    height: 1136px;
    background: var(--label-yellow);
    overflow: hidden;
  }
  .label-art {
    position: absolute;
    inset: 0;
    width: 660px;
    height: 1136px;
  }
  .flavor-name {
    position: absolute;
    top: 34px;
    left: 184px;
    width: 368px;
    text-align: center;
    font-family: "Anton", sans-serif;
    font-size: 62px;
    line-height: 1.1;
    letter-spacing: 1px;
    color: var(--label-yellow);
    -webkit-text-stroke: 2px var(--outline-green);
  }
  .brand-name {
    position: absolute;
    top: 300px;
    left: 0;
    width: 660px;
    text-align: center;
    font-family: "Anton", sans-serif;
    font-size: 220px;
    line-height: 1.2;
    color: var(--ink);
  }
  .product-line {
    position: absolute;
    top: 856px;
    left: 165px;
    display: flex;
    align-items: baseline;
    gap: 12px;
    white-space: nowrap;
  }
  .product-tea {
    font-family: "Roboto Condensed", sans-serif;
    font-weight: 400;
    font-size: 76px;
    line-height: 1;
    color: var(--white);
    -webkit-text-stroke: 2px var(--ink);
  }
  .product-electrolytes {
    font-family: "Anton", sans-serif;
    font-size: 46px;
    line-height: 1;
    color: var(--band-green);
    -webkit-text-stroke: 1px #0d6a0d;
  }
  .category-band {
    position: absolute;
    top: 938px;
    left: 109px;
    width: 551px;
    height: 72px;
  }
  .category-text {
    position: absolute;
    top: 952px;
    left: 155px;
    font-family: "Montserrat", sans-serif;
    font-weight: 700;
    font-size: 36px;
    line-height: 1.2;
    letter-spacing: 16px;
    color: var(--white);
    white-space: nowrap;
  }
  .volume {
    position: absolute;
    top: 1078px;
    left: 139px;
    font-family: "Roboto Condensed", sans-serif;
    font-weight: 700;
    font-size: 44px;
    line-height: 1.1;
    color: var(--volume-ink);
    white-space: nowrap;
  }
</style>
</head>
<body>
<main class="canvas">
  <section class="label">
    <svg class="label-art" viewBox="0 0 660 1136" xmlns="http://www.w3.org/2000/svg">
      <defs>
        <linearGradient id="cyclist-fill" x1="0" y1="0" x2="0" y2="1">
          <stop offset="0" stop-color="var(--cyclist-tone-b)"/>
          <stop offset="1" stop-color="var(--cyclist-tone-a)"/>
        </linearGradient>
        <linearGradient id="runner-fill" x1="0" y1="0" x2="0" y2="1">
          <stop offset="0" stop-color="var(--runner-tone-a)"/>
          <stop offset="1" stop-color="var(--runner-tone-b)"/>
        </linearGradient>
      </defs>
      <polygon class="accent-stripe" points="192,0 601,0 109,1136 0,1136 0,393" fill="var(--label-green)"/>
      <path role="img" aria-label="Mountain biker in helmet riding toward the viewer, green tinted photo"
            d="M170,150 Q230,110 300,150 L370,420 L330,760 L170,1136 L25,1136 L50,520 L90,300 Z"
            fill="url(#cyclist-fill)" opacity="0.75"/>
      <path role="img" aria-label="Female runner in sports top, muted sepia tinted photo"
            d="M520,92 Q580,80 610,150 L660,260 L660,1095 L530,1095 L400,820 L430,420 L470,230 Z"
            fill="url(#runner-fill)" opacity="0.72"/>
    </svg>

    <div class="flavor-name">PINEAPPLE</div>
    <div class="brand-name">VANTO</div>

    <div class="product-line">
      <span class="product-tea">TEA</span>
      <span class="product-electrolytes">+ELECTROLYTES</span>
    </div>

    <svg class="category-band" viewBox="0 0 551 72" xmlns="http://www.w3.org/2000/svg">
      <polygon points="24,4 551,4 551,68 4,68" fill="var(--band-green)" stroke="var(--ink)" stroke-width="4"/>
    </svg>
    <div class="category-text">SPORTS TEA</div>

    <div class="volume">16 fl.oz.(474ml)</div>
  </section>
</main>
</body>
</html>
```